Kinesiology undergraduate program needs an infographic

We would like an infographic to creatively and succinctly inform students, faculty, staff, and others about our undergraduate values and competencies (perhaps also integrating our mission and vision). We would like to see a design that incorporates the definition of Kinesiology (the study of human movement) and the colors of our Northbrook Lakeshore State University.

```html
<!DOCTYPE html>
<html lang="en">
<head>
<meta charset="UTF-8">
<title>Kinesiology – The study of human movement</title>
<link rel="stylesheet" href="https://fonts.googleapis.com/css2?family=Oswald:wght@700&family=Fira+Sans:wght@400;600&display=swap">
<style>
  :root {
    --bg-cream: #f3eee0;
    --bg-lilac: #e6dcec;
    --bg-mint: #e4ebe6;
    --band: #ea9772;
    --ink: #161616;
    --ink-soft: #1f1f1f;
    --silhouette: #8f8f8f;
    --muscle-light: #e8a98c;
    --muscle-deep: #c2684c;
  }
  html, body {
    margin: 0;
    padding: 0;
    width: 1200px;
    height: 800px;
    overflow: hidden;
  }
  .infographic {
    position: relative;
    width: 1200px;
    height: 800px;
    overflow: hidden;
    background:
      linear-gradient(160deg, var(--bg-lilac) 0%, var(--bg-mint) 18%, var(--bg-cream) 45%, var(--bg-cream) 72%, var(--bg-lilac) 100%);
    font-family: "Fira Sans", Arial, sans-serif;
    color: var(--ink);
  }
  .streaks {
    position: absolute;
    inset: 0;
    background: repeating-linear-gradient(60deg, rgba(255,255,255,0) 0 60px, rgba(255,255,255,0.22) 60px 64px, rgba(255,255,255,0) 64px 140px);
  }
  .title {
    position: absolute;
    left: 0;
    width: 1164px;
    top: 14px;
    margin: 0;
    text-align: center;
    font-family: "Oswald", Impact, sans-serif;
    font-weight: 700;
    font-size: 57px;
    letter-spacing: 2px;
    line-height: 1;
    color: var(--ink);
  }
  .subtitle {
    position: absolute;
    left: 0;
    width: 1164px;
    top: 72px;
    margin: 0;
    text-align: center;
    font-size: 28px;
    font-weight: 400;
    letter-spacing: 0.5px;
    color: var(--ink);
  }
  .section-band {
    position: absolute;
    left: 0;
    width: 556px;
    height: 32px;
    background: var(--band);
    clip-path: polygon(0 0, 100% 0, 98.2% 100%, 0 100%);
  }
  .section-title {
    position: absolute;
    left: 48px;
    margin: 0;
    font-size: 22px;
    font-weight: 600;
    letter-spacing: 1.4px;
    line-height: 32px;
    color: var(--ink);
    white-space: nowrap;
  }
  .competency-list {
    position: absolute;
    left: 60px;
    margin: 0;
    padding: 0;
    list-style: none;
  }
  .competency-list li {
    position: relative;
    padding-left: 15px;
    height: 30px;
    line-height: 30px;
    font-size: 18px;
    letter-spacing: 0.5px;
    color: var(--ink-soft);
    white-space: nowrap;
  }
  .competency-list li::before {
    content: "";
    position: absolute;
    left: 2px;
    top: 12px;
    width: 6px;
    height: 6px;
    border-radius: 50%;
    background: var(--ink);
  }
  .athlete {
    position: absolute;
    background: var(--silhouette);
    opacity: 0.55;
    border-radius: 40px;
  }
  .athlete--cyclist { left: 48px; top: 24px; width: 128px; height: 112px; }
  .athlete--footballer { left: 1064px; top: 8px; width: 126px; height: 182px; }
  .athlete--basketball { left: 556px; top: 594px; width: 92px; height: 206px; opacity: 0.45; }
  .athlete--runner { left: 1002px; top: 598px; width: 186px; height: 202px; opacity: 0.45; }
  .anatomy-figure {
    position: absolute;
    left: 622px;
    top: 164px;
    width: 506px;
    height: 532px;
  }
</style>
</head>
<body>
<main class="infographic">
  <div class="streaks"></div>

  <div class="athlete athlete--cyclist" role="img" aria-label="Grey silhouette of a road cyclist riding a bicycle"></div>
  <div class="athlete athlete--footballer" role="img" aria-label="Grey silhouette of a soccer player dribbling a ball"></div>
  <div class="athlete athlete--basketball" role="img" aria-label="Grey silhouette of a basketball player leaping to dunk"></div>
  <div class="athlete athlete--runner" role="img" aria-label="Grey silhouette of a sprinter running"></div>

  <svg class="anatomy-figure" viewBox="0 0 506 532" role="img" aria-label="Anatomical illustration of the human muscular system, front view, arms outstretched">
    <defs>
      <radialGradient id="muscle-tone" cx="50%" cy="40%" r="60%">
        <stop offset="0%" stop-color="var(--muscle-light)" stop-opacity="0.75"/>
        <stop offset="100%" stop-color="var(--muscle-deep)" stop-opacity="0.15"/>
      </radialGradient>
    </defs>
    <rect x="0" y="0" width="506" height="532" rx="60" fill="url(#muscle-tone)"/>
  </svg>

  <h1 class="title">KINESIOLOGY</h1>
  <p class="subtitle">The study of human movement</p>

  <div class="section-band" style="top:138px"></div>
  <h2 class="section-title" style="top:138px">THE SCIENCE OF KINESIOLOGY</h2>
  <ul class="competency-list" style="top:174px">
    <li>Foundational Concepts of Kinesiology</li>
    <li>Clinical Application</li>
    <li>Scientific Communication</li>
  </ul>

  <div class="section-band" style="top:271px"></div>
  <h2 class="section-title" style="top:271px">THINKING AND REASONING</h2>
  <ul class="competency-list" style="top:307px">
    <li>Critical Thinking</li>
    <li>Quantitative Reasoning</li>
    <li>Scientific Inquiry</li>
    <li>Concept Integration</li>
  </ul>

  <div class="section-band" style="top:434px"></div>
  <h2 class="section-title" style="top:434px">RELATIONSHIPS AND COMMUNICATION</h2>
  <ul class="competency-list" style="top:470px">
    <li>Cultural Competence</li>
    <li>Professionalism</li>
    <li>Leadership and Teamwork</li>
    <li>Service Orientation/Citizenship</li>
  </ul>

  <div class="section-band" style="top:597px"></div>
  <h2 class="section-title" style="top:597px">INTRAPERSONAL GROWTH</h2>
  <ul class="competency-list" style="top:631px">
    <li>Cultural Humility/Sensitivity</li>
    <li>Integrity</li>
    <li>Self-Directed</li>
    <li>Dependability</li>
    <li>Mission Oriented</li>
  </ul>
</main>
</body>
</html>
```